lunetra.com redesign

We are a successful web hosting company that has been around since 1999 with 10,000 customers managing 2,000 websites and 12,000 domain names. Our challenge - we are losing ground because our site is getting old, our pricing is not competitive and our feature set needs to change to match the new world of mobile centric everything. We want to reach out to all of the domain names that we don't host websites for. We believe that if we designed a new site that focuses on bringing home all of those externally hosted websites to our own web hosting company that we would have a solid future. We need to compete against mopwizzle.com, vantrimble.com, kerbloom.com, zinqhut.com, nolvark.com, brimfolk.com, quorvane.com, welbix.com and 100,000 others. We need to simplify our message with clean design, focused pages, easy decision making processes for the consumer. We use WHMCS for the background provisioning and billing so we can pretty much manage any kind of pricing model and discounted promotion packages.
I would prefer Twitter bootstrap CSS based responsive design.

Reason: I was away on vacation for 2 weeks - I just got back - I need time to fairly review all submissions - thank you for your patience. Dorian Fenwick Lunetra.com

Thanks to all who submitted sample designs - unfortunately most of them were nothing much more than already available templates with some of my current content and logo added to them. I will try to be more specific to reduce the number of choices. I need the template be fully compatible with WHMCS and Wordpress if you can't make it work with WHMCS directly. Another question I have to ask is -"exactly what am I getting for my $500.00 - is it just a PSD template or actual integration of that theme into WHMCS or Wordpress?"  I don't expect anyone to create new content for the site at that price. What do you charge if  you are able to create content or get directly involved in the site implementation of that template?

```html
<!DOCTYPE html>
<html lang="en">
<head>
<meta charset="utf-8">
<title>Lunetra – Web Hosting</title>
<link href="https://fonts.googleapis.com/css2?family=Montserrat:wght@400;500;600;700&family=Open+Sans:wght@400;600;700&display=swap" rel="stylesheet">
<style>
:root{
  --blue:#1a7fd4;
  --navy:#0d4f8e;
  --navy-dark:#0a3f73;
  --sky:#a6c3e8;
  --btn:#2b8fe6;
  --green-head:#c6e3a2;
  --green-body:#e0f8c9;
  --green-ribbon:#6fa35a;
  --mint:#d6f3ec;
  --teal:#21a3c9;
  --ink:#1f2f3f;
  --text:#555;
  --muted:#777;
  --grey-band:#ececec;
  --icon-grey:#c9c9c9;
  --footer:#2b2b2b;
  --footer-low:#1d1d1d;
  --footer-text:#9a9a9a;
  --white:#fff;
}
*{box-sizing:border-box;margin:0;padding:0}
html,body{width:694px;height:1200px;overflow:hidden;background:var(--white)}
body{position:relative;font-family:"Open Sans",Arial,sans-serif;color:var(--text)}
.abs{position:absolute}

/* header */
.header{position:absolute;left:0;top:0;width:694px;height:62px;background:linear-gradient(#1c87db,#1671c3)}
.toplinks{position:absolute;left:82px;top:3px;font:600 7px "Montserrat",sans-serif;color:var(--white)}
.toplinks span{margin-right:5px}
.account{position:absolute;right:82px;top:3px;font:600 7px "Montserrat",sans-serif;color:var(--white)}
.account span{margin-left:12px}
.logo{position:absolute;left:82px;top:20px;font:700 30px "Montserrat",sans-serif;color:var(--white);letter-spacing:-1px}
.service{position:absolute;left:252px;top:35px;font:500 7.5px "Montserrat",sans-serif;color:var(--white)}
.livechat{position:absolute;left:432px;top:33px;font:500 8px "Montserrat",sans-serif;color:var(--white);display:flex;align-items:center;gap:5px}
.search{position:absolute;left:505px;top:30px;width:107px;height:18px;background:var(--white);border-radius:3px;font-size:6px;color:#999;padding:5px 0 0 5px}
.search svg{position:absolute;right:5px;top:4px}

.nav{position:absolute;left:0;top:62px;width:694px;height:25px;background:var(--navy-dark);display:flex;padding-left:82px}
.nav a{font:500 8px "Montserrat",sans-serif;color:var(--white);text-decoration:none;line-height:25px;margin-right:16px}

/* hero */
.hero{position:absolute;left:0;top:87px;width:694px;height:225px;background:linear-gradient(90deg,#7d8a93 0%,#a7b1b8 35%,#c9ced2 60%,#5c5f63 78%,#d5d8da 100%)}
.hero-card{position:absolute;left:108px;top:104px;width:192px;height:192px;border-radius:50%;background:rgba(255,255,255,.88);text-align:center}
.hero-card h1{font:600 15px/18px "Montserrat",sans-serif;color:var(--navy);margin-top:36px;letter-spacing:.5px}
.hero-card p{font-size:7.5px;line-height:12px;color:var(--navy);margin-top:7px}
.feats{display:grid;grid-template-columns:70px 60px;justify-content:center;gap:2px 10px;margin-top:8px;text-align:left;font-size:7.5px;color:var(--navy)}
.feats span{display:flex;align-items:center;gap:3px}
.btn{display:inline-flex;align-items:center;background:var(--btn);color:var(--white);font:500 7.5px "Montserrat",sans-serif;height:23px;border-radius:2px;overflow:hidden}
.btn i{display:flex;align-items:center;justify-content:center;width:25px;height:23px;background:var(--navy)}
.btn b{font-weight:500;padding:0 9px 0 8px}
.hero-card .btn{margin-top:8px}

/* domain */
.domainbar{position:absolute;left:0;top:312px;width:694px;height:34px;background:var(--sky)}
.domainbar .lbl{position:absolute;top:12px;font:600 8px "Montserrat",sans-serif;color:var(--ink);letter-spacing:.5px}
.field{position:absolute;top:6px;height:22px;background:var(--white);font-size:7px;color:#888;padding:7px 8px}
.tld{position:absolute;left:472px;top:6px;width:50px;height:22px;background:#eef1f4;font-size:7px;color:#666;padding:7px 8px}
.tld svg{position:absolute;right:7px;top:9px}
.search-btn{position:absolute;left:533px;top:6px;width:60px;height:22px;background:var(--btn);color:var(--white);font:600 7px "Montserrat",sans-serif;text-align:center;line-height:22px;border-radius:2px}

/* packages */
.packages{position:absolute;left:82px;top:368px;width:333px;height:113px;background:var(--green-body)}
.packages h2{height:22px;background:var(--green-head);text-align:center;font:600 8.5px/22px "Montserrat",sans-serif;color:var(--ink);letter-spacing:.5px}
.packages table{border-collapse:collapse;margin:5px 0 0 10px;font:500 7.5px "Montserrat",sans-serif;color:var(--ink)}
.packages th{font-weight:600;text-align:left;height:16px}
.packages td{height:16px}
.c1{width:39px}.c2{width:50px}.c3{width:73px}.c4{width:86px}

.promo{position:absolute;left:433px;top:368px;width:179px;height:113px;background:var(--mint);text-align:center;overflow:hidden}
.promo .l1{font:600 9.5px "Montserrat",sans-serif;color:var(--ink);margin-top:10px;letter-spacing:.5px}
.promo .l2{font:500 16px "Montserrat",sans-serif;color:var(--teal);margin-top:4px;letter-spacing:1px}
.promo .l3{font:600 9px "Montserrat",sans-serif;color:var(--ink);margin-top:5px;letter-spacing:.5px}
.promo .btn{margin-top:11px}
.ribbon{position:absolute;right:-22px;top:10px;width:90px;transform:rotate(45deg);background:var(--green-ribbon);color:var(--white);font:600 5px/7px "Montserrat",sans-serif;padding:2px 0;text-align:center}

/* services */
.sec-title{position:absolute;left:0;width:694px;text-align:center;font:600 14px "Montserrat",sans-serif;color:var(--ink);letter-spacing:1.5px}
.sec-sub{position:absolute;left:0;width:694px;text-align:center;font-size:7.5px;color:var(--text)}
.svc{position:absolute;width:230px}
.svc .ic{position:absolute;left:0;top:0;width:32px;height:32px;border-radius:50%;background:var(--icon-grey)}
.svc h3{position:absolute;left:50px;top:4px;font:500 10px "Montserrat",sans-serif;color:var(--ink);letter-spacing:.8px}
.svc p{position:absolute;left:50px;top:22px;width:180px;font-size:7px;line-height:13px;color:var(--text)}

/* about band */
.band{position:absolute;left:0;top:677px;width:694px;height:280px;background:var(--grey-band)}
.band h2{position:absolute;left:0;top:12px;width:694px;text-align:center;font:700 14px "Montserrat",sans-serif;color:var(--ink)}
.band .sub{position:absolute;left:0;top:33px;width:694px;text-align:center;font-size:7.5px;color:#444}
.point{position:absolute;font-size:6.8px;line-height:9.5px;color:var(--muted)}
.point h4{font:600 7.5px "Montserrat",sans-serif;color:var(--ink);margin-bottom:3px;white-space:nowrap}
.left .point{width:125px;text-align:right}
.right .point{width:140px}
.servers{position:absolute;left:260px;top:745px;width:170px;height:172px;background:linear-gradient(160deg,#5a5a5a,#1a1a1a 55%,#ececec 56%,#d8dbe6 70%,#2a3570 85%)}

/* footer */
.footer{position:absolute;left:0;top:957px;width:694px;height:215px;background:var(--footer)}
.fcol{position:absolute;top:14px;font-size:6px;line-height:9.5px;color:var(--footer-text)}
.fcol h5{font:600 9.5px "Montserrat",sans-serif;color:var(--white);margin-bottom:6px;letter-spacing:.3px}
.fcol ul{list-style:none;font:500 6px/13.5px "Montserrat",sans-serif}
.socials{display:flex;gap:2px}
.socials span{width:17px;height:17px;border-radius:50%;background:#5a5a5a}
.chatbtn{position:absolute;left:535px;top:87px;width:77px;height:24px;background:#3c3c3c;border-radius:2px;color:var(--white);font:500 8px "Montserrat",sans-serif;display:flex;align-items:center;gap:9px;padding-left:7px}
.newsletter{position:absolute;left:82px;top:178px;display:flex;align-items:center;gap:5px;font:600 8px/8px "Montserrat",sans-serif;color:var(--white)}
.news-in{position:absolute;left:160px;top:179px;width:117px;height:17px;background:#1c1c1c;border:1px solid #555;font-size:6px;color:#aaa;padding:4px 5px}
.subscribe{position:absolute;left:282px;top:179px;width:47px;height:17px;background:var(--btn);color:var(--white);font:600 6px/17px "Montserrat",sans-serif;text-align:center}
.accept{position:absolute;left:388px;top:179px;font:600 7.5px/9px "Montserrat",sans-serif;color:var(--white)}
.cards{position:absolute;left:461px;top:177px;display:flex;gap:5px}
.cards span{height:21px;background:var(--white);border-radius:2px;font:700 7px/21px "Montserrat",sans-serif;color:var(--navy);text-align:center}
.bottom{position:absolute;left:0;top:1172px;width:694px;height:28px;background:var(--footer-low);font-size:6px;color:#999}
.legal{position:absolute;left:82px;top:10px}
.legal span{margin:0 7px}
.legal span:first-child{margin-left:0}
.copy{position:absolute;right:82px;top:10px}
</style>
</head>
<body>

<header class="header">
  <div class="toplinks"><span>COMPANY</span><span>PARTNERS</span><span>SUPPORT</span><span>CONTACT US</span><span style="margin-left:8px">REFERENCES</span><span>PRICING</span></div>
  <div class="account"><span>&#128722; SHOPPING CART</span><span>&#8676; LOGIN</span><span>&#9998; REGISTER</span></div>
  <div class="logo">lunetra</div>
  <div class="service">24X7 CUSTOMER SERVICE &nbsp;800-555-0147</div>
  <div class="livechat">
    <svg width="12" height="10" viewBox="0 0 12 10"><path d="M1 1h7v5H4L2 8V6H1z" fill="#fff"/><path d="M9 3h2v4h-1v2L8 7H5V6.5h3.5V3z" fill="#fff"/></svg>
    LIVE CHAT
  </div>
  <div class="search">Search
    <svg width="9" height="9" viewBox="0 0 9 9"><circle cx="3.6" cy="3.6" r="2.6" fill="none" stroke="#999" stroke-width="1"/><path d="M5.5 5.5L8 8" stroke="#999" stroke-width="1.2"/></svg>
  </div>
</header>

<nav class="nav">
  <a>HOME</a><a>DOMAIN NAME CENTER</a><a>WEB SITE HOSTING CENTER</a><a>S.E.O. TOOLKIT</a><a>SUPPORT</a><a>CLIENT AREA</a><a>CONTACT</a>
</nav>

<section class="hero" role="img" aria-label="Photo of a businessman in a suit standing in a server room"></section>
<div class="hero-card">
  <h1>LUNETRA EOLITE<br>PACKAGE</h1>
  <p>everthing you need for your<br>business to succed online</p>
  <div class="feats">
    <span><svg width="9" height="7" viewBox="0 0 9 7"><path d="M1 3.5l2.5 2.5L8 1" stroke="#5fa83a" stroke-width="1.8" fill="none"/></svg>Domain Name</span>
    <span><svg width="9" height="7" viewBox="0 0 9 7"><path d="M1 3.5l2.5 2.5L8 1" stroke="#5fa83a" stroke-width="1.8" fill="none"/></svg>Email</span>
    <span><svg width="9" height="7" viewBox="0 0 9 7"><path d="M1 3.5l2.5 2.5L8 1" stroke="#5fa83a" stroke-width="1.8" fill="none"/></svg>Hosting</span>
    <span><svg width="9" height="7" viewBox="0 0 9 7"><path d="M1 3.5l2.5 2.5L8 1" stroke="#5fa83a" stroke-width="1.8" fill="none"/></svg>Site Builder</span>
  </div>
  <div class="btn"><i><svg width="11" height="9" viewBox="0 0 11 9"><path d="M10 4.5H3M10 4.5L7 1.5M10 4.5L7 7.5" stroke="#fff" stroke-width="1.5" fill="none"/></svg></i><b>SING UP NOW</b></div>
</div>

<section class="domainbar">
  <span class="lbl" style="left:100px">FIND YOUR DOMAIN NAME</span>
  <span class="lbl" style="left:240px">WWW.</span>
  <div class="field" style="left:278px;width:183px">enter a domain name</div>
  <div class="tld">.com<svg width="6" height="4" viewBox="0 0 6 4"><path d="M0 0h6L3 4z" fill="#888"/></svg></div>
  <div class="search-btn">SEARCH</div>
</section>

<section class="packages">
  <h2>CHOOSE A HOSTING PACKAGE</h2>
  <table>
    <tr><th class="c1"></th><th class="c2">STORAGE</th><th class="c3">DOMAIN NAME</th><th class="c4">EMAIL ACCOUNTS</th><th>ANNUAL PRICE</th></tr>
    <tr><td>e-lite</td><td>100 MB</td><td>Included</td><td>Unlimited</td><td>$90</td></tr>
    <tr><td>e-200</td><td>200 MB</td><td>Included</td><td>Unlimited</td><td>$149</td></tr>
    <tr><td>e-500</td><td>500 MB</td><td>Included</td><td>Unlimited</td><td>$249</td></tr>
    <tr><td>e-1000</td><td>10000 MB</td><td>Included</td><td>Unlimited</td><td>$549</td></tr>
  </table>
</section>

<aside class="promo">
  <div class="ribbon">LIMITED<br>TIME OFFER</div>
  <div class="l1">GET UP TO</div>
  <div class="l2">25% DISCOUNT</div>
  <div class="l3">ON ALL HOSTING ORDERS</div>
  <div class="btn"><i><svg width="11" height="9" viewBox="0 0 11 9"><path d="M10 4.5H3M10 4.5L7 1.5M10 4.5L7 7.5" stroke="#fff" stroke-width="1.5" fill="none"/></svg></i><b>SING UP NOW</b></div>
</aside>

<h2 class="sec-title" style="top:500px">SERVICES</h2>
<p class="sec-sub" style="top:521px">Get These free services and many more with all accounts</p>

<div class="svc" style="left:82px;top:550px"><span class="ic"></span><h3>EASY TRANSFER</h3><p>Switching to Lunetra from another host is easy: sit back while we take care of everything.</p></div>
<div class="svc" style="left:384px;top:550px"><span class="ic"></span><h3>SITE BUILDER</h3><p>With SiteBuilder, you can build your website with drag-and-drop simplicity.</p></div>
<div class="svc" style="left:82px;top:609px"><span class="ic"></span><h3>SCRIPTDECK</h3><p>Over 50 essential scripts for building your web-site installed in minutes with a click.</p></div>
<div class="svc" style="left:384px;top:609px"><span class="ic"></span><h3>BE FOUND</h3><p>We include search engine positioning with every plan, so your customers can find your website.</p></div>

<section class="band">
  <h2>Lunetra Makes it easy to get online</h2>
  <p class="sub">Lunetra has been recognized as a leader in business</p>
</section>

<div class="left">
  <div class="point" style="left:110px;top:731px"><h4>About Lunetra</h4>As an RDAO-accredited regis-<br>trar for more than 10 years,<br>Lunetra is a leading provider of</div>
  <div class="point" style="left:110px;top:784px"><h4>Domain Registration</h4>Registering a domain is the first<br>step in building your website.<br>Choose from dozens of domain</div>
  <div class="point" style="left:110px;top:835px"><h4>Website Hosting</h4>Lunetra's website hosting plans<br>are fast, flexible and affordable.<br>We offer plans to meet your</div>
  <div class="point" style="left:110px;top:887px"><h4>24/7 Customer Service</h4>All Lunetra products come with<br>free 24/7 support. For more<br>information about Lunetra cus-</div>
</div>
<div class="right">
  <div class="point" style="left:445px;top:731px"><h4>Email Hosting</h4>Email hosting lets you create<br>personalized email accounts at<br>the domain of your choice.</div>
  <div class="point" style="left:445px;top:782px"><h4>SiteBuilder</h4>Included free with every hosting<br>plan, Lunetra's premium<br>SiteBuilder lets anyone easily</div>
  <div class="point" style="left:445px;top:834px"><h4>Business Solutions</h4>Lunetra provides a variety of<br>business and marketing solu-<br>tions for small business custom-</div>
  <div class="point" style="left:445px;top:886px"><h4>More Reasons to Choose Lunetra</h4>As an award winning, premium<br>provider of Internet services for<br>small businesses and individuals,</div>
</div>

<div class="servers" role="img" aria-label="Illustration of three black server towers with an award badge and ribbon"></div>

<footer class="footer">
  <div class="fcol" style="left:82px;width:90px">
    <h5>ABOUT US</h5>
    As an RDAO-accredited regis-trar for more than 10 years, Lunetra is a leading provider of domain registration, website hosting, website design, and email hosting for small and medium-sized businesses. Lunetra has helped tens of thousands of businesses and individuals establish their web presence, build their websites, and drive revenue
  </div>
  <div class="fcol" style="left:198px;width:78px">
    <h5>POLICY</h5>
    All Transactions are based on US or Canadi-an Dollars. lunetra.com is registered and located in Norland<br><br>
    90 day refund guaran-tee on all purchases. No refunds on hosting services already provid-ed.
  </div>
  <div class="fcol" style="left:299px">
    <h5>OUR LINK</h5>
    <ul><li>HOME</li><li>DOMAIN NAME CENTER</li><li>WEB SITE HOSTING CENTER</li><li>S.E.O. TOOLKIT</li><li>SUPPORT</li><li>CLIENT AREA</li><li>CONTACT</li></ul>
  </div>
  <div class="fcol" style="left:411px;line-height:13.5px">
    <h5>CONTACT US</h5>
    42 Harlow Lane<br>Brindlemoor<br>Eastmark Q1R 3T4<br>Norland<br>
    800-555-0147 or 800-555-0193<br>800-555-0128<br>info@lunetra.com
  </div>
  <div class="fcol" style="left:538px">
    <h5>FALLOW US</h5>
    <div class="socials"><span></span><span></span><span></span><span></span></div>
  </div>
  <div class="chatbtn">
    <svg width="14" height="11" viewBox="0 0 12 10"><path d="M1 1h7v5H4L2 8V6H1z" fill="#bbb"/><path d="M9 3h2v4h-1v2L8 7H5V6.5h3.5V3z" fill="#bbb"/></svg>
    LIVE CHAT
  </div>

  <div class="newsletter">
    <svg width="13" height="11" viewBox="0 0 13 11"><path d="M0 5L13 0 10 11 6 7z" fill="#888"/></svg>
    <span>NEWSLETTER<br>SIGN UP</span>
  </div>
  <div class="news-in">Enter your email address</div>
  <div class="subscribe">SUBSCRIBE</div>
  <div class="accept">WE ACCEPT<br>PAYMENT FROM</div>
  <div class="cards">
    <span style="width:41px">Cardly</span>
    <span style="width:38px">Paymint</span>
    <span style="width:63px">Coinrail</span>
  </div>
</footer>

<div class="bottom">
  <div class="legal"><span>Terms of Use</span>|<span>Dispute Policy</span>|<span>Disclaimer</span>|<span>Privacy Policy</span>|<span>Refund Policy</span>|<span>Refund Policy</span></div>
  <div class="copy">Copyright © 2014 Lunetra. All Rights Reserved.</div>
</div>

</body>
</html>
```